THE TALL COPPER ATLAS OF PORTS

subtitle: AN INTRO TO SEARCH ENGINE OPTIMIZATION
background: white
dimensions: 1562x2500

Target Market(s)

Marketing professionals

Industry/Entity Type

Digital Marketing

Font styles to use
Sans Serif

Colors
ffffff
1b1b1b
3176b5

Requirements
Should not have
• Images or graphics

```html
<!DOCTYPE html>
<html lang="en">
<head>
<meta charset="utf-8">
<title>The Tall Copper Atlas of Ports — Book Cover</title>
<link rel="stylesheet" href="https://fonts.googleapis.com/css2?family=Montserrat:wght@800&family=Oswald:wght@500;600&display=swap">
<style>
  :root {
    --page-bg: #e4e4e4;
    --cover-light: #f0f0f0;
    --brand-blue: #3176b5;
    --ink: #1b1b1b;
    --white: #ffffff;
    --accent-yellow: #f5c518;
    --author-grey: #8a8a8a;
  }
  html, body {
    margin: 0;
    padding: 0;
    width: 1200px;
    height: 1200px;
    overflow: hidden;
    background: var(--page-bg);
  }
  .book-cover {
    position: absolute;
    left: 250px;
    top: 40px;
    width: 700px;
    height: 1120px;
    background: var(--cover-light);
    overflow: hidden;
  }
  .title-band {
    position: absolute;
    left: 0;
    top: 0;
    width: 100%;
    height: 418px;
    background: var(--brand-blue);
  }
  .title-lead {
    position: absolute;
    left: 84px;
    top: 190px;
    margin: 0;
    font-family: "Montserrat", sans-serif;
    font-weight: 800;
    font-size: 58px;
    line-height: 64px;
    letter-spacing: 0.5px;
    color: var(--white);
  }
  .accent-square {
    position: absolute;
    left: 0;
    top: 383px;
    width: 59px;
    height: 71px;
    background: var(--accent-yellow);
  }
  .title-main {
    position: absolute;
    left: 66px;
    top: 440px;
    margin: 0;
    font-family: "Montserrat", sans-serif;
    font-weight: 800;
    font-size: 170px;
    line-height: 1;
    letter-spacing: -4px;
    color: var(--ink);
  }
  .subtitle {
    position: absolute;
    left: 80px;
    top: 640px;
    margin: 0;
    font-family: "Oswald", sans-serif;
    font-weight: 500;
    font-size: 28px;
    line-height: 1;
    letter-spacing: 1.5px;
    color: var(--ink);
  }
  .author-name {
    position: absolute;
    left: 95px;
    top: 994px;
    margin: 0;
    font-family: "Oswald", sans-serif;
    font-weight: 600;
    font-size: 50px;
    line-height: 1;
    letter-spacing: 2px;
    color: var(--author-grey);
  }
</style>
</head>
<body>
  <main class="book-cover">
    <div class="title-band"></div>
    <h1 class="title-lead">THE TALL<br>COPPER ATLAS<br>OF</h1>
    <div class="accent-square"></div>
    <p class="title-main">PORTS</p>
    <p class="subtitle">AN INTRO TO SEARCH ENGINE OPTIMIZATION</p>
    <p class="author-name">DANIEL HOLMVIK</p>
  </main>
</body>
</html>
```